Pelling Home Efficiency

Id like for my business card to be very bold and professional. Incorporating the business logo, the main services offered, and my contact info. Services are spray foam, insulation, new construction, retrofit, weatherization.

When opening this project art huddle was not able to upload my new logo that I picked from another recent art huddle project. Does anyone know how i could upload my logo onto the page for design of the business cards?

Target Market(s)

Building owners, contractors

Industry/Entity Type

Building Insulation and performance improvements

Contact Information for Business Card

Owner, Email marcus@pellinghomeefficiency.com Phone number 555-204-6817

Colors
0054AA
0677BA
7BADD7
CADEEF
E8F1F8
F0912C
F2A743
F7CA91
FBE8D2
FDF5EE

Requirements
Must have
• Services- spray foam, cellulose, mineral wool, fiberglass, air sealing, new construction, retrofit, weatherization, energy saving assesments

```html
<!DOCTYPE html>
<html lang="en">
<head>
<meta charset="utf-8">
<title>Pelling Home Efficiency – Business Card</title>
<link rel="stylesheet" href="https://fonts.googleapis.com/css2?family=Archivo:wght@400;500;700;800;900&display=swap">
<style>
  :root {
    --stage: #2b2b2b;
    --navy: #0b1634;
    --white: #ffffff;
    --orange: #f0742c;
    --blue: #35ace3;
    --ink: #1d1d1f;
  }
  * { box-sizing: border-box; margin: 0; padding: 0; }
  html, body { width: 1200px; height: 875px; overflow: hidden; }
  body {
    background: var(--stage);
    font-family: "Archivo", Arial, sans-serif;
    position: relative;
  }
  .card {
    position: absolute;
    width: 540px;
    height: 309px;
    border-radius: 18px;
    overflow: hidden;
    box-shadow: 0 20px 40px rgba(0,0,0,.45);
  }
  /* Front */
  .card--front { left: 30px; top: 120px; background: var(--navy); color: var(--white); }
  .brand {
    position: absolute; left: 0; right: 0; top: 78px;
    display: flex; align-items: center; justify-content: center; gap: 14px;
  }
  .brand__mark { width: 26px; height: 26px; background: var(--blue); }
  .brand__name {
    font-weight: 900; font-size: 30px; letter-spacing: .5px;
    color: var(--orange); text-transform: uppercase; line-height: 1;
  }
  .services {
    position: absolute; left: 0; right: 0; top: 178px;
    text-align: center; font-size: 13.5px; font-weight: 500;
    letter-spacing: .4px; line-height: 1.75; text-transform: uppercase;
  }
  .services .tick {
    display: inline-block; width: 11px; height: 11px; vertical-align: -1px;
    margin: 0 6px;
  }
  /* Back */
  .card--back { left: 630px; top: 440px; background: var(--white); }
  .back__brand {
    position: absolute; left: 30px; top: 128px; width: 210px;
    display: flex; align-items: center; gap: 10px;
  }
  .back__brand .brand__mark { width: 16px; height: 16px; flex: none; }
  .back__brand .brand__name { font-size: 17px; }
  .divider {
    position: absolute; left: 262px; top: 74px; width: 1.5px; height: 130px;
    background: var(--blue);
  }
  .person { position: absolute; left: 286px; top: 78px; }
  .person__name {
    font-weight: 800; font-size: 25px; color: var(--blue);
    text-transform: uppercase; letter-spacing: .3px;
  }
  .person__role { font-size: 14px; color: var(--orange); margin: 2px 0 12px; }
  .contact { list-style: none; font-size: 13px; color: var(--ink); }
  .contact li { display: flex; align-items: center; gap: 9px; margin-bottom: 6px; }
  .contact svg { width: 12px; height: 12px; flex: none; }
  .band {
    position: absolute; left: 0; right: 0; bottom: 0; height: 8px;
    background: linear-gradient(90deg, var(--blue) 0 78%, var(--orange) 78% 100%);
  }
</style>
</head>
<body>
  <svg width="0" height="0" style="position:absolute">
    <symbol id="tick" viewBox="0 0 12 12">
      <circle cx="6" cy="6" r="6" fill="#f0742c"/>
      <path d="M3.3 6.2l1.8 1.8 3.6-3.8" fill="none" stroke="#0b1634" stroke-width="1.6" stroke-linecap="round" stroke-linejoin="round"/>
    </symbol>
  </svg>

  <section class="card card--front" aria-label="Card front">
    <div class="brand">
      <span class="brand__mark"></span>
      <span class="brand__name">Pelling Home Efficiency</span>
    </div>
    <p class="services">
      Spray Foam<svg class="tick"><use href="#tick"/></svg>Cellulose<svg class="tick"><use href="#tick"/></svg>Mineral Wool<br>
      Fiberglass<svg class="tick"><use href="#tick"/></svg>Air Sealing<svg class="tick"><use href="#tick"/></svg>New Construction<svg class="tick"><use href="#tick"/></svg>Retrofit<br>
      Weatherization<svg class="tick"><use href="#tick"/></svg>Energy Saving Assesments
    </p>
  </section>

  <section class="card card--back" aria-label="Card back">
    <div class="back__brand">
      <span class="brand__mark"></span>
      <span class="brand__name">Pelling Home Efficiency</span>
    </div>
    <div class="divider"></div>
    <div class="person">
      <h1 class="person__name">Marcus Dale</h1>
      <p class="person__role">Owner</p>
      <ul class="contact">
        <li>
          <svg viewBox="0 0 12 12"><path d="M2.5 1h2l1 2.6-1.3 1a6 6 0 0 0 3.2 3.2l1-1.3L11 7.5v2a1.5 1.5 0 0 1-1.5 1.5A8.5 8.5 0 0 1 1 2.5 1.5 1.5 0 0 1 2.5 1z" fill="#f0742c"/></svg>
          555-204-6817
        </li>
        <li>
          <svg viewBox="0 0 12 12"><rect x="0.5" y="2" width="11" height="8" rx="1" fill="#f0742c"/><path d="M1 2.8l5 3.6 5-3.6" fill="none" stroke="#fff" stroke-width="1"/></svg>
          marcus@pellinghomeefficiency.com
        </li>
        <li>
          <svg viewBox="0 0 12 12"><circle cx="6" cy="6" r="5" fill="none" stroke="#f0742c" stroke-width="1.4"/><path d="M1 6h10M6 1c2 2.5 2 7.5 0 10M6 1c-2 2.5-2 7.5 0 10" fill="none" stroke="#f0742c" stroke-width="1"/></svg>
          pellinghomeefficiency.com
        </li>
      </ul>
    </div>
    <div class="band"></div>
  </section>
</body>
</html>
```